Pell Consulting -New consulting business in architecture, urban planning, and real estate development

We need a stationery design, including logo, business cards, etc, work for a new consulting business that works in the world of architectural, urban planning and real estate development.

The name of the company is "Pell Consulting". Pell is my last name but it of course also has the meaning 'cool' and 'hip'.

Target Market(s)

The business will provide boutique consulting services to high end clients that may include property developers, cities, etc.

Industry/Entity Type

Consultant

Contact Information for Business Card

PELL Consulting
First Name Last Name
Title
Phone number
Address
Website
Optional: Twitter handle

Logo Text

PELL Consulting

Font styles to use
Sans Serif

Colors

Designer to choose colors to be used in the design.

Requirements
Must have
• Simple design
• Easy to read font
• Modern
• Elegance
• Nice font that can be used for future reports, letters, etc.
• Good colour scheme that allows for the elegance to come through
Should not have
• Complex design ideas
• Complex logos
• Not a corporate feel and look

```html
<!DOCTYPE html>
<html lang="en">
<head>
<meta charset="utf-8">
<title>Pell Consulting – Business Card</title>
<link href="https://fonts.googleapis.com/css2?family=Montserrat:wght@400;500;700;800&display=swap" rel="stylesheet">
<style>
  :root {
    --page-bg: #ececea;
    --card-white: #ffffff;
    --gold: #a68a2b;
    --gold-deep: #9c8127;
    --ink: #2e2e2e;
    --ink-soft: #4a4a4a;
  }
  * { box-sizing: border-box; margin: 0; padding: 0; }
  html, body {
    width: 1200px; height: 1127px; overflow: hidden;
    background: var(--page-bg);
    font-family: "Montserrat", sans-serif;
  }
  .sheet {
    position: relative; width: 1200px; height: 1127px;
    display: flex; align-items: center; justify-content: center; gap: 40px;
  }
  .card {
    position: relative; width: 540px; height: 309px;
    box-shadow: 0 2px 6px rgba(0,0,0,.08);
  }
  /* front */
  .card--front { background: var(--card-white); }
  .brand {
    position: absolute; left: 42px; top: 108px; width: 200px;
    color: var(--gold); font-weight: 500; text-align: center;
  }
  .brand__name { display: block; font-size: 60px; line-height: 1; letter-spacing: 2px; }
  .brand__sub { display: block; font-size: 11px; letter-spacing: 6px; margin-top: 4px; }
  .divider {
    position: absolute; left: 272px; top: 70px; width: 1px; height: 170px;
    background: var(--gold);
  }
  .details { position: absolute; left: 298px; top: 74px; color: var(--ink-soft); }
  .details__name { font-size: 17px; font-weight: 800; color: var(--ink); letter-spacing: .2px; }
  .details__title { font-size: 11px; margin-top: 2px; }
  .details__address { font-size: 11px; line-height: 15px; margin-top: 8px; padding-left: 20px; }
  .contact { list-style: none; margin-top: 8px; font-size: 11px; }
  .contact li { display: flex; align-items: center; height: 15px; }
  .contact svg { width: 11px; height: 11px; margin-right: 9px; flex: none; }
  .contact .blank { width: 11px; margin-right: 9px; }
  /* back */
  .card--back { background: var(--gold); overflow: hidden; }
  .card__pattern {
    position: absolute; inset: 0;
    background: radial-gradient(circle at 50% 50%, #ad9233 0%, var(--gold-deep) 100%);
  }
  .brand--reverse {
    left: 170px; top: 100px; color: #ffffff;
  }
</style>
</head>
<body>
<main class="sheet">
  <section class="card card--front" aria-label="Business card front">
    <div class="brand">
      <span class="brand__name">PELL</span>
      <span class="brand__sub">CONSULTING</span>
    </div>
    <div class="divider"></div>
    <div class="details">
      <p class="details__name">Daniel MORROW</p>
      <p class="details__title">Managing Director</p>
      <p class="details__address">214 N Harbor Avenue<br>Ashford, MS 39150</p>
      <ul class="contact">
        <li>
          <svg viewBox="0 0 12 12" fill="var(--gold)"><path d="M2.5 1l2 2.3-1 1.2c.8 1.6 2 2.8 3.5 3.5l1.2-1L10.5 9 9.3 10.8C5 10.5 1.5 7 1.2 2.6z"/></svg>
          000.000.0000
        </li>
        <li>
          <svg viewBox="0 0 12 12" fill="none" stroke="var(--gold)" stroke-width="1.2"><rect x="3" y="1" width="6" height="10" rx="1"/></svg>
          000.000.0000
        </li>
        <li>
          <svg viewBox="0 0 12 12" fill="none" stroke="var(--gold)" stroke-width="1.1"><rect x="1" y="2.5" width="10" height="7"/><path d="M1 2.5l5 4 5-4"/></svg>
          daniel@pellconsulting.com
        </li>
        <li>
          <svg viewBox="0 0 12 12" fill="none" stroke="var(--gold)" stroke-width="1"><circle cx="6" cy="6" r="5"/><ellipse cx="6" cy="6" rx="2.2" ry="5"/><path d="M1 6h10M2 3.5h8M2 8.5h8"/></svg>
          www.pellconsulting.com
        </li>
      </ul>
    </div>
  </section>

  <section class="card card--back" aria-label="Business card back">
    <div class="card__pattern" role="img" aria-label="Tonal gold ornamental lace pattern covering the card"></div>
    <div class="brand brand--reverse">
      <span class="brand__name">PELL</span>
      <span class="brand__sub">CONSULTING</span>
    </div>
  </section>
</main>
</body>
</html>
```